Maple Ridge business card design

Card needs to include the following text/items:
Company Logo
Tobin Marsh
Phone # - 555-318-7642
service@mapleridgelandscaping.example
Lawn & landscape maintenance services

```html
<!DOCTYPE html>
<html lang="en">
<head>
<meta charset="utf-8">
<title>Maple Ridge Landscaping – Business Card</title>
<link href="https://fonts.googleapis.com/css2?family=Lato:wght@400;700;900&display=swap" rel="stylesheet">
<style>
  :root {
    --bg: #cbcbcb;
    --card-white: #ffffff;
    --brand-green: #21613a;
    --text-grey: #555555;
    --band-white: #ffffff;
    --scene-sky: #dcecef;
    --scene-ground: #b9c8b0;
    --scene-ring: #cfe3c4;
    --mark-fill: #8fb89a;
    --shadow: rgba(0, 0, 0, 0.28);
  }
  * { margin: 0; padding: 0; box-sizing: border-box; }
  html, body {
    width: 1200px; height: 800px; overflow: hidden;
    background: var(--bg);
    font-family: "Lato", sans-serif;
  }
  .stage { position: relative; width: 1200px; height: 800px; }
  .card {
    position: absolute; left: 424px; width: 420px; height: 240px;
    border-radius: 12px; overflow: hidden;
    box-shadow: 2px 3px 4px var(--shadow);
  }
  .card--front { top: 130px; background: var(--card-white); }
  .card--back { top: 430px; background: var(--brand-green); }

  .front__scene {
    position: absolute; left: 207px; top: 5px; width: 290px; height: 290px;
    border-radius: 50%;
    border: 3px solid var(--scene-ring);
    background: linear-gradient(180deg, var(--scene-sky) 0%, #e6ecdf 45%, var(--scene-ground) 100%);
    opacity: 0.85;
  }
  .front__brand {
    position: absolute; left: 31px; top: 32px;
    font-size: 19px; font-weight: 900; color: var(--brand-green);
    line-height: 20px; letter-spacing: 1px; text-transform: uppercase;
  }
  .front__name {
    position: absolute; left: 31px; top: 115px;
    font-size: 20px; font-weight: 900; color: var(--brand-green);
    letter-spacing: 0.2px; line-height: 24px;
  }
  .front__title {
    position: absolute; left: 31px; top: 140px;
    font-size: 11.5px; line-height: 16px; color: var(--text-grey);
  }
  .contact-list {
    position: absolute; left: 31px; top: 169px; list-style: none;
  }
  .contact-list li {
    position: relative;
    display: flex; align-items: center; height: 17.5px;
    font-size: 12px; color: var(--text-grey);
  }
  .contact-list svg { width: 11px; height: 11px; margin-right: 10px; fill: var(--brand-green); }

  .back__mark {
    position: absolute; left: 155px; top: 33px; width: 108px; height: 108px;
    border-radius: 50%; background: var(--mark-fill);
  }
  .back__brand {
    position: absolute; left: 0; right: 0; top: 142px; text-align: center;
    font-size: 17px; font-weight: 900; color: var(--card-white);
    line-height: 17px; letter-spacing: 1px; text-transform: uppercase;
  }
  .services-band {
    position: absolute; left: 0; right: 0; top: 197px; height: 19px;
    background: var(--band-white);
    display: flex; align-items: center; justify-content: center;
    font-size: 10px; color: var(--brand-green);
  }
  .services-band .sep { margin: 0 5px; }
</style>
</head>
<body>
<main class="stage">
  <section class="card card--front">
    <div class="front__scene" role="img" aria-label="Faded landscape illustration with trees, hill, sun and fence"></div>
    <div class="front__brand">Maple Ridge<br>Landscaping</div>
    <div class="front__name">TOBIN MARSH</div>
    <div class="front__title">Founder</div>
    <ul class="contact-list">
      <li>
        <svg viewBox="0 0 24 24" aria-hidden="true"><path d="M6.6 10.8a15 15 0 0 0 6.6 6.6l2.2-2.2c.3-.3.7-.4 1-.2 1.1.4 2.3.6 3.6.6.6 0 1 .4 1 1V20c0 .6-.4 1-1 1A17 17 0 0 1 3 4c0-.6.4-1 1-1h3.5c.6 0 1 .4 1 1 0 1.3.2 2.5.6 3.6.1.3 0 .7-.2 1z"/></svg>
        555-318-7642
      </li>
      <li>
        <svg viewBox="0 0 24 24" aria-hidden="true"><path d="M2 5h20v14H2z M3 6l9 7 9-7" stroke="#fff" stroke-width="1.5"/></svg>
        service@mapleridgelandscaping.example
      </li>
      <li>
        <svg viewBox="0 0 24 24" aria-hidden="true"><circle cx="12" cy="12" r="10" fill="none" stroke="#21613a" stroke-width="2"/><path d="M2 12h20M12 2c3 3 3 17 0 20M12 2c-3 3-3 17 0 20" fill="none" stroke="#21613a" stroke-width="1.5"/></svg>
        www.mapleridgelandscaping.example
      </li>
    </ul>
  </section>

  <section class="card card--back">
    <div class="back__mark" aria-hidden="true"></div>
    <div class="back__brand">Maple Ridge<br>Landscaping</div>
    <div class="services-band">
      <span>Lawn Mowing Service</span><span class="sep">||</span>
      <span>Raking Service</span><span class="sep">||</span>
      <span>Trimming &amp; Edging</span><span class="sep">||</span>
      <span>Basic Gardening.</span>
    </div>
  </section>
</main>
</body>
</html>
```